Silver Heron Construction Services

Create a business card for my business consulting company
Danielle Vesk, Founder and CEO
4816 Alder Brook Way, Ste 100
Denver, CO. 80451
303.782.4190 cell
dvesk@silverheronconst.example
www.silverheronconst.example

Target Market(s)

Private Equity and Construction Companies

Industry/Entity Type

Business / Sales Consulting

Contact Information for Business Card

Tag Line that says "Where The Road To Success Is Always Under Construction"

Requirements
Must have
• Logo on both sides of the card.
Nice to have
• Add tagline to the same side of the card as my name and contact info

```html
<!DOCTYPE html>
<html lang="en">
<head>
<meta charset="utf-8">
<title>Silver Heron Construction Services – Business Card</title>
<link href="https://fonts.googleapis.com/css2?family=Arimo:wght@400;700&display=swap" rel="stylesheet">
<style>
  :root {
    --backdrop: #3b3b3b;
    --ink: #111111;
    --paper: #ffffff;
    --muted: #7a7a7a;
    --rule: #c8c8c8;
  }
  * { margin: 0; padding: 0; box-sizing: border-box; }
  html, body {
    width: 1200px; height: 689px; overflow: hidden;
    background: var(--backdrop);
    font-family: "Arimo", Arial, sans-serif;
  }
  .stage { position: relative; width: 1200px; height: 689px; }
  .card {
    position: absolute; top: 190px;
    width: 540px; height: 309px;
    border-radius: 16px; overflow: hidden;
  }
  .card-back { left: 40px; background: var(--ink); }
  .card-front { left: 620px; background: var(--paper); }

  /* Back side */
  .back-brand {
    position: absolute; left: 0; right: 0; top: 50%;
    transform: translateY(-50%);
    display: flex; align-items: center; justify-content: center; gap: 14px;
    color: var(--paper);
  }
  .brand-square { width: 22px; height: 22px; background: var(--paper); }
  .back-brand .brand-name {
    font-weight: 700; font-size: 24px; letter-spacing: 1px; text-transform: uppercase;
  }

  /* Front side */
  .front-brand {
    position: absolute; left: 30px; top: 96px; width: 220px;
    display: flex; align-items: center; gap: 10px; color: var(--ink);
  }
  .front-brand .brand-square { width: 16px; height: 16px; background: var(--ink); flex: none; }
  .front-brand .brand-name {
    font-weight: 700; font-size: 19px; line-height: 1.15; text-transform: uppercase;
  }
  .divider {
    position: absolute; left: 268px; top: 40px; width: 1px; height: 150px;
    background: linear-gradient(var(--paper), var(--rule) 30%, var(--rule) 70%, var(--paper));
  }
  .contact { position: absolute; left: 290px; top: 40px; color: var(--ink); }
  .person-name { font-weight: 700; font-size: 22px; text-transform: uppercase; }
  .person-title { font-size: 12px; color: var(--muted); margin-top: 2px; }
  .address { font-size: 12.5px; color: var(--muted); line-height: 1.35; margin-top: 14px; }
  .contact-lines { margin-top: 12px; font-size: 12.5px; color: var(--muted); line-height: 1.5; }
  .contact-line { display: flex; align-items: center; gap: 8px; }
  .contact-line svg { width: 10px; height: 10px; fill: var(--ink); flex: none; }
  .tagline {
    position: absolute; left: 30px; bottom: 34px;
    font-size: 13px; color: var(--ink);
  }
  .web-band {
    position: absolute; right: 0; bottom: 0; width: 250px; height: 64px;
  }
  .web-band svg { position: absolute; inset: 0; }
  .web-band .url {
    position: absolute; right: 18px; bottom: 12px;
    font-size: 12.5px; color: var(--paper);
  }
</style>
</head>
<body>
<div class="stage">
  <section class="card card-back" aria-label="Card back">
    <div class="back-brand">
      <span class="brand-square"></span>
      <span class="brand-name">Silver Heron</span>
    </div>
  </section>

  <section class="card card-front" aria-label="Card front">
    <div class="front-brand">
      <span class="brand-square"></span>
      <span class="brand-name">Silver Heron Construction Services</span>
    </div>
    <div class="divider"></div>
    <div class="contact">
      <div class="person-name">Danielle Vesk</div>
      <div class="person-title">Founder and CEO</div>
      <div class="address">4816 Alder Brook Way<br>Ste 100<br>Denver, CO. 80451</div>
      <div class="contact-lines">
        <div class="contact-line">
          <svg viewBox="0 0 10 10"><path d="M2 0.5 L3.8 2.5 L2.8 3.6 Q4 6 6.4 7.2 L7.5 6.2 L9.5 8 L8.3 9.5 Q3.5 9 0.5 1.7 Z"/></svg>
          <span>303.782.4190 cell</span>
        </div>
        <div class="contact-line">
          <svg viewBox="0 0 10 10"><path d="M0 2 H10 V8.5 H0 Z M0.8 2.6 L5 5.6 L9.2 2.6 Z" fill-rule="evenodd"/></svg>
          <span>dvesk@silverheronconst.example</span>
        </div>
      </div>
    </div>
    <div class="tagline">The Road To Success Is Always Under Construction</div>
    <div class="web-band">
      <svg viewBox="0 0 250 64" preserveAspectRatio="none"><path d="M0 64 L0 40 L14 40 L14 30 L250 30 L250 64 Z" fill="#111111"/></svg>
      <span class="url">www.silverheronconst.example</span>
    </div>
  </section>
</div>
</body>
</html>
```